依頼詳細
高級住宅地、オフィス街を対象に配るA4チラシ(片面)になります。高級感溢れるデザインをお願いいたします。
印刷はミドリカゼを使用する予定です。入稿可能なAiファイルでの作成をお願いいたします。
https://midorikaze-example.jp/dataguide/

色選びはカラーパレットをご使用ください。
記載項目
記載内容は添付のワードファイルをご参照ください。
講師プロフィール用の写真は仮の写真です。決定いたしまた方に後ほど実際に使用いただく写真をお渡しいたします。
イメージ画像を1枚添付しておりますが、使用はお任せいたします。
サイズ
A4
ページ数
片面
希望イメージ
シンプル 複雑
単色 カラフル
暗い 明るい
日常 高級
遊び心 厳粛
未来的 伝統的
女性的 男性的
希望する色
黄・オレンジ系、青系、無彩色系
納品ファイル
• イラストレーター形式 (.ai)
補足説明
当初の設定ミスで募集期間5日間としていましたが、3日間に訂正いたします。
期間が短くなりますが、どうぞよろしくお願いいたします。
報酬金額変更いたしました。
どうぞよろしくお願いいたします。
提出ファイル形式についての追記です。
採用に至った場合は、そのまま入稿できるAiファイルと後に文字を編集する予定があるためテキストをアウトライン化する前(テキスト部分が後に編集できるもの)のファイルの2種類の提出をお願いいたします。可能であればWindows Adobe Illustrator CS4対応のファイル形式でお願いします。また、特殊なフォントをご使用の場合は一緒にご提出願います。
お手数おかけいたしますがよろしくお願いいたします。

ターゲットを意識した画像の使用、レイアウト、高級感とすべてよかったです。

この度はコンペにご参加いただきありがとうございました。
予想以上に多くの提案をいただきまして大変感謝いたしております。
多数の素晴らしいご提案から選ぶのに時間がかかりまして、
お待たせいたしましたことをお詫び申し上げます。
また、機会がございましたらどうぞよろしくお願いいたします。

```html
<!DOCTYPE html>
<html lang="ja">
<head>
<meta charset="utf-8">
<title>KEIRA 完全プライベート英会話レッスン</title>
<link rel="stylesheet" href="https://fonts.googleapis.com/css2?family=Noto+Serif+JP:wght@400;600;700&family=Noto+Sans+JP:wght@400;700&family=Cinzel:wght@600&display=swap">
<style>
:root{
  --brown-dark:#2e1b12;
  --brown:#4a2e1f;
  --brown-mid:#6b4530;
  --gold:#c9974a;
  --gold-light:#e7c58a;
  --cream:#f4ead9;
  --ink:#3a2418;
  --white:#fff;
}
*{margin:0;padding:0;box-sizing:border-box}
html,body{width:856px;height:1200px;overflow:hidden}
body{background:var(--brown-dark);font-family:"Noto Serif JP",serif;color:var(--ink);position:relative}
.hero{position:absolute;left:0;top:0;width:856px;height:430px;
  background:linear-gradient(90deg,#3b2519 0%,#5a3a28 45%,#6e4a33 70%,#3a2418 100%)}
.hero-photo{position:absolute;right:0;top:0;width:520px;height:300px;
  background:radial-gradient(ellipse at 60% 45%,#8a6548 0%,#5a3b29 55%,rgba(58,36,24,0) 80%)}
.brand{position:absolute;left:0;top:24px;width:190px;height:92px;background:var(--brown);
  display:flex;align-items:center;justify-content:center;
  font-family:"Cinzel",serif;font-weight:600;font-size:40px;color:var(--white);letter-spacing:2px}
.title{position:absolute;left:0;width:856px;top:205px;text-align:center;color:var(--white);
  font-size:34px;font-weight:600;letter-spacing:1px}
.subtitle{position:absolute;left:0;width:856px;top:256px;text-align:center;color:var(--white);font-size:24px;font-weight:600}
.lead{position:absolute;left:120px;width:616px;top:300px;text-align:center;color:var(--gold-light);font-size:12px;line-height:1.7}
.offer{position:absolute;left:0;top:430px;width:856px;height:140px;background:var(--brown-dark);text-align:center}
.offer-label{display:inline-block;margin-top:18px;background:var(--gold);color:var(--brown-dark);padding:3px 26px;font-size:18px;font-weight:700}
.offer-text{color:var(--gold-light);font-size:15px;line-height:1.6;margin-top:8px}
.offer-note{color:var(--gold);font-size:11px;margin-top:4px}
.message{position:absolute;left:0;top:570px;width:856px;height:88px;background:var(--brown);text-align:center;border-top:2px solid var(--gold);border-bottom:2px solid var(--gold)}
.message-head{color:var(--gold-light);font-size:12px;margin-top:6px}
.message-en{color:var(--white);font-size:22px;font-weight:700;font-style:italic;margin-top:2px}
.message-ja{color:var(--gold-light);font-size:14px;margin-top:2px}
.body{position:absolute;left:0;top:658px;width:856px;height:507px;background:var(--cream)}
.col{position:absolute;top:16px}
.col-why{left:24px;width:262px}
.col-profile{left:300px;width:256px}
.col-info{left:572px;width:260px}
.why-head{font-size:20px;font-weight:700;line-height:1.35;color:var(--brown);border-bottom:1px solid var(--gold);padding-bottom:8px}
.why-list{list-style:none;margin-top:10px}
.why-list li{font-size:11px;line-height:1.65;margin-bottom:9px;font-family:"Noto Sans JP",sans-serif}
.why-list li::before{content:"■ ";color:var(--gold)}
.profile-head{background:var(--brown);color:var(--white);font-size:12px;text-align:center;padding:3px}
.profile-photo{width:110px;height:140px;margin:10px 0 0 0;float:left;background:linear-gradient(180deg,#bfa88c,#7b5b43)}
.profile-text{font-size:10px;line-height:1.6;font-family:"Noto Sans JP",sans-serif;margin-top:10px}
.profile-text p{margin-bottom:6px}
.profile-top{margin-left:120px;padding-top:10px}
.info-head{background:var(--brown);color:var(--white);font-size:13px;padding:3px 10px;margin-bottom:8px}
.faq p,.lesson p{font-size:10.5px;line-height:1.6;font-family:"Noto Sans JP",sans-serif;margin-bottom:6px}
.faq .q{color:var(--brown-mid);font-weight:700}
.lesson{margin-top:12px}
.footer{position:absolute;left:0;top:1165px;width:856px;height:35px;background:var(--brown-dark);
  color:var(--white);font-size:18px;font-weight:600;display:flex;align-items:center;justify-content:center;gap:24px}
.footer-small{font-size:12px;color:var(--gold-light);position:absolute;top:1146px;width:856px;text-align:center}
</style>
</head>
<body>
<section class="hero">
  <div class="hero-photo" role="img" aria-label="スーツ姿の男性がオフィスで微笑む写真"></div>
  <div class="brand">KEIRA</div>
  <h1 class="title">ワンランク上の完全プライベート英会話レッスン</h1>
  <p class="subtitle">― 全てにおいて最高品質を求める貴方へ ―</p>
  <p class="lead">経営者、医師、弁護士、役員など、多忙なエグゼクティブのための完全個別英会話レッスンです。<br>経験豊富な講師が、ご希望の時間と場所で、目的に合わせた最高の授業をお届けします。</p>
</section>

<section class="offer">
  <span class="offer-label">限定案内</span>
  <p class="offer-text">エグゼクティブの方々から大好評をいただいております、<br>ジョン・ミラー（講師）のレッスンに１枠空きが出ました。</p>
  <p class="offer-note">受付は先着順となります。お早めにお問い合わせください。</p>
</section>

<section class="message">
  <p class="message-head">【講師ジョン・ミラーのメッセージ】</p>
  <p class="message-en">“My goal is to make the country of Japan stronger, one person at a time.”</p>
  <p class="message-ja">「 私のゴールは、一人ずつから日本という国を強くすることです。」</p>
</section>

<section class="body">
  <div class="col col-why">
    <h2 class="why-head">なぜ、ジョンのレッスンは<br>そんなに人気なのか？</h2>
    <ul class="why-list">
      <li>１対１の完全個別指導で、受講者の目標とレベルに合わせて内容を組み立てます。</li>
      <li>ビジネスの現場で長年活躍した経験から、実践的な英語表現を学べます。</li>
      <li>会議、交渉、会食など具体的な場面を想定し、すぐに使える力を養います。</li>
      <li>ご自宅やオフィスなど、ご希望の場所と時間に合わせて柔軟に対応します。</li>
      <li>丁寧で温かい人柄により、初めての方でも安心して続けることができます。</li>
    </ul>
  </div>

  <div class="col col-profile">
    <p class="profile-head">講師プロフィール</p>
    <div class="profile-photo" role="img" aria-label="講師の上半身のポートレート写真"></div>
    <div class="profile-top profile-text">
      <p><b>講師 ジョン・ミラー</b></p>
      <p>米国出身。大学で経営学を修めた後、国際企業で長年勤務。</p>
      <p>来日後、企業研修や個人指導で多くの実績を持つ。</p>
    </div>
    <div class="profile-text" style="clear:both">
      <p>これまで経営者や医師など、数多くのエグゼクティブの英語力向上を支援してきました。</p>
      <p>趣味は読書と旅行。日本の文化を深く愛しています。</p>
      <p>「英語を通して、皆様の可能性を世界へ広げるお手伝いをいたします。」</p>
    </div>
  </div>

  <div class="col col-info">
    <p class="info-head">FAQ</p>
    <div class="faq">
      <p><span class="q">Q.</span> 初心者でも受講できますか？<br>A. はい、レベルに合わせて丁寧に指導します。</p>
      <p><span class="q">Q.</span> レッスン場所は選べますか？<br>A. ご自宅、オフィスなどご希望に対応します。</p>
      <p><span class="q">Q.</span> 体験レッスンはありますか？<br>A. 初回は無料でお試しいただけます。</p>
    </div>
    <div class="lesson">
      <p class="info-head">レッスン案内</p>
      <p>時間：1回 60分〜90分<br>曜日：月曜日〜土曜日（応相談）<br>場所：ご指定の場所へ伺います</p>
      <p class="info-head" style="margin-top:10px">料金</p>
      <p>入会金：無料<br>月4回コース：お問い合わせください<br>※交通費は別途となります</p>
    </div>
  </div>
</section>

<p class="footer-small">ご質問等ございましたら、お気軽にお問い合わせください。</p>
<footer class="footer">
  <span>Email keira@example-mail.jp</span>
  <span>Tel 092-555-0147</span>
  <span>携帯 080-5555-0192</span>
</footer>
</body>
</html>
```